Tampa Bay fishing guide needs stunning website.

I currently have a site - www.reelcoveguide.example which I personally put together using the Plixo platform and I am looking for a redesign on a different platform (Brindlepress?) that will allow me to easily create landing pages in the future. Would like to have a block for visitors to opt in to newsletter. Need social media links on all pages.
Updates

I would like to let my visitors know that I am able to handle their fishing charter needs here in the Tampa Bay area, if I'm not available for the dates they are looking to go I can refer them to a reputable captain in the area.

Target Market(s)

United States

Industry/Entity Type

Tourism

Coding

Coded - Design and coding required

Number of Pages Required

5+ page

Font styles to use
Sans Serif

Colors
0355a3
3176b5
85abd2
fbf289

Requirements
Must have
• Mobile Responsive, Ability to insert Vantor Metrics, Quillbook pixels, ability to add custom landing pages in future
Nice to have
• Clean, easy navigation

```html
<!DOCTYPE html>
<html lang="en">
<head>
<meta charset="utf-8">
<title>Capt. Wade Harlow Sport Fishing</title>
<link href="https://fonts.googleapis.com/css2?family=Montserrat:wght@500;600;700;800&family=Open+Sans:ital,wght@0,400;0,600;1,400&display=swap" rel="stylesheet">
<style>
:root{
  --blue:#0355a3;
  --blue-mid:#3176b5;
  --blue-light:#85abd2;
  --yellow:#fbf289;
  --gold:#f5c33b;
  --navy:#0b1a2c;
  --navy-dark:#07111d;
  --grey-bg:#f1f0f1;
  --text:#5a5a5a;
  --white:#ffffff;
}
*{box-sizing:border-box;margin:0;padding:0}
html,body{width:1200px;height:2623px;overflow:hidden}
body{font-family:"Open Sans",sans-serif;color:var(--text);background:var(--white);position:relative}
.heading{font-family:"Montserrat",sans-serif;font-weight:800;color:var(--blue);text-transform:uppercase;text-align:center}
.eyebrow{font-size:12px;color:var(--blue-mid);text-align:center}
.btn{display:inline-block;background:var(--gold);color:#3a2c00;font-family:"Montserrat",sans-serif;font-weight:700;font-size:15px;text-transform:uppercase;padding:11px 26px;border-radius:3px}

/* top bar */
.topbar{position:absolute;top:0;left:0;width:1200px;height:28px;background:var(--blue);display:flex;align-items:center;justify-content:space-between;padding:0 160px}
.topbar-links{display:flex;gap:10px}
.topbar-links span{border:1px solid var(--gold);color:var(--white);font-size:10px;font-weight:600;padding:2px 8px;border-radius:2px;display:flex;align-items:center;gap:5px;text-transform:uppercase}
.topbar-call{color:var(--white);font-size:11px;font-weight:600;display:flex;align-items:center;gap:6px;text-transform:uppercase}

/* header */
.site-header{position:absolute;top:28px;left:0;width:1200px;height:92px;background:var(--white);display:flex;align-items:center;justify-content:space-between;padding:0 160px 0 160px}
.brand{display:flex;align-items:center;gap:10px;font-family:"Montserrat",sans-serif;font-weight:800;font-size:34px;color:var(--blue)}
.brand i{display:block;width:14px;height:14px;border-radius:50%;background:var(--blue-mid)}
.nav{display:flex;gap:32px;font-family:"Montserrat",sans-serif;font-size:13px;font-weight:600;color:#333;text-transform:uppercase}
.nav .active{border-bottom:2px solid var(--blue);padding-bottom:3px}

/* hero */
.hero{position:absolute;top:120px;left:0;width:1200px;height:475px;background:linear-gradient(180deg,#566d6a 0%,#6f8a86 30%,#3f6e92 60%,#2d5d8c 100%);text-align:center}
.hero-title{position:absolute;top:225px;left:0;width:100%;font-family:"Montserrat",sans-serif;font-weight:800;font-size:44px;line-height:48px;color:var(--gold);text-transform:uppercase;text-shadow:0 2px 6px rgba(0,0,0,.45)}
.hero-sub{position:absolute;top:335px;left:0;width:100%;font-family:"Montserrat",sans-serif;font-weight:700;font-size:19px;line-height:28px;color:var(--white);text-shadow:0 2px 5px rgba(0,0,0,.5)}
.hero .btn{position:absolute;top:400px;left:536px}
.hero-arrow{position:absolute;top:178px}

/* intro */
.intro{position:absolute;top:595px;left:0;width:1200px;height:410px;padding-top:50px}
.intro .heading{font-size:27px;margin-top:14px}
.intro-copy{width:830px;margin:22px auto 0;text-align:center;font-size:11px;line-height:23px}
.badges{display:flex;justify-content:center;gap:14px;margin-top:16px}
.badge{width:112px;height:96px;border:1px solid #c9c9c9;background:var(--white);position:relative}
.badge.green::before{content:"";position:absolute;top:0;left:0;right:0;height:22px;background:#5b9c3a}
.badge.navy{border-color:var(--blue)}
.badge.navy::after{content:"";position:absolute;bottom:0;left:0;right:0;height:16px;background:var(--blue)}

/* locations */
.locations{position:absolute;top:1005px;left:0;width:1200px;height:635px;background:var(--grey-bg);padding-top:57px}
.locations .heading{font-size:27px;margin-top:12px}
.map{position:absolute;top:125px;left:164px;width:874px;height:391px;background:linear-gradient(135deg,#cfe3c4 0%,#e8e6da 45%,#d7e5cd 70%,#bcd6ec 100%);border:2px solid var(--white)}
.map-card{position:absolute;top:166px;left:20px;width:180px;padding:10px 12px;background:var(--white);font-family:"Montserrat",sans-serif;font-weight:700;font-size:11px;line-height:15px;color:var(--blue);text-transform:uppercase;box-shadow:0 1px 4px rgba(0,0,0,.3)}
.map-pin{position:absolute;top:246px;left:40px}
.locations .btn{position:absolute;top:540px;left:522px}

/* plans */
.plans{position:absolute;top:1640px;left:0;width:1200px;height:354px}
.plans .heading{font-size:27px;position:absolute;top:40px;width:100%}
.plan{position:absolute;top:1749px;width:280px;height:192px}
.plan-photo{height:150px;position:relative}
.plan-tag{position:absolute;top:0;left:0;background:var(--gold);color:#2a2000;font-family:"Montserrat",sans-serif;font-weight:700;font-size:12px;padding:4px 8px;text-transform:uppercase}
.plan-price{height:42px;background:var(--blue);text-align:center;font-family:"Montserrat",sans-serif;font-weight:700;font-size:13px;line-height:18px;color:var(--gold);padding-top:4px;text-transform:uppercase}

/* testimonials */
.testimonials{position:absolute;top:1994px;left:0;width:1200px;height:356px;background:linear-gradient(180deg,#0a4f9a 0%,#0355a3 50%,#0b4d93 100%);text-align:center}
.testimonials .eyebrow{color:var(--white);margin-top:52px}
.testimonials .heading{color:var(--white);font-size:30px;margin-top:4px}
.quote{position:absolute;top:112px;width:278px;text-align:center}
.quote-box{background:var(--white);height:98px;padding:22px 20px;font-size:12px;line-height:20px;color:#555;position:relative}
.quote-box::after{content:"";position:absolute;left:50%;bottom:-10px;margin-left:-10px;border-left:10px solid transparent;border-right:10px solid transparent;border-top:10px solid var(--white)}
.quote-box b{font-family:Georgia,serif;color:#333;font-size:14px}
.quote-name{margin-top:28px;font-family:"Montserrat",sans-serif;font-weight:700;font-size:14px;color:var(--gold);text-transform:uppercase}
.quote-role{font-size:12px;font-style:italic;color:var(--white);margin-top:4px}
.dots{position:absolute;top:290px;left:582px;display:flex;gap:4px}
.dots i{width:8px;height:8px;border-radius:50%;border:1px solid var(--white)}
.dots i.on{background:var(--white)}

/* footer */
.site-footer{position:absolute;top:2350px;left:0;width:1200px;height:230px;background:var(--navy)}
.contact{position:absolute;top:48px;left:160px;font-size:12px;line-height:18px;color:var(--white)}
.contact-row{display:flex;gap:14px;margin-bottom:22px;align-items:flex-start}
.divider{position:absolute;top:45px;width:1px;height:140px;background:rgba(255,255,255,.12)}
.info{position:absolute;top:46px;left:460px}
.info h4{font-family:"Montserrat",sans-serif;font-weight:700;font-size:15px;color:var(--gold);text-transform:uppercase;margin-bottom:12px}
.info-links{display:grid;grid-template-columns:150px 100px;row-gap:8px;font-size:12px;color:var(--white)}
.footer-badges{position:absolute;top:55px;left:793px;display:flex;gap:14px}
.socials{position:absolute;top:188px;left:934px;display:flex;gap:8px}
.socials i{width:18px;height:18px;border-radius:2px}
.copyright{position:absolute;top:2580px;left:0;width:1200px;height:43px;background:var(--navy-dark);color:var(--white);font-size:11px;padding:14px 160px}
</style>
</head>
<body>

<div class="topbar">
  <div class="topbar-links">
    <span><svg width="10" height="9" viewBox="0 0 10 9"><rect x="0.5" y="3" width="9" height="5.5" fill="none" stroke="#f5c33b"/><rect x="0" y="1" width="10" height="2.5" fill="#f5c33b"/></svg>Gift Card</span>
    <span><svg width="10" height="9" viewBox="0 0 10 9"><path d="M0 4 10 0 7 9 5 5Z" fill="#f5c33b"/></svg>Newsletter</span>
  </div>
  <div class="topbar-call">
    <svg width="11" height="11" viewBox="0 0 24 24"><path d="M6.6 10.8a15 15 0 0 0 6.6 6.6l2.2-2.2c.3-.3.7-.4 1-.2 1.1.4 2.3.6 3.6.6.6 0 1 .4 1 1V20c0 .6-.4 1-1 1A17 17 0 0 1 3 4c0-.6.4-1 1-1h3.5c.6 0 1 .4 1 1 0 1.3.2 2.5.6 3.6.1.3 0 .7-.2 1z" fill="#fff"/></svg>
    Call Capt. Wade (555) 201-4438
  </div>
</div>

<header class="site-header">
  <div class="brand"><i></i>Harlow</div>
  <nav class="nav">
    <span class="active">Home</span><span>About Us</span><span>Pick Up Locations</span><span>Rates</span><span>Gallery</span><span>Contact</span>
  </nav>
</header>

<section class="hero" role="img" aria-label="Photo of the captain standing on the tower of a flats boat docked in a mangrove-lined canal">
  <svg class="hero-arrow" style="left:160px" width="26" height="60" viewBox="0 0 26 60"><path d="M24 2 2 30l22 28" fill="none" stroke="#fff" stroke-width="2"/></svg>
  <svg class="hero-arrow" style="left:1012px" width="26" height="60" viewBox="0 0 26 60"><path d="M2 2l22 28L2 58" fill="none" stroke="#fff" stroke-width="2"/></svg>
  <h1 class="hero-title">Capt. Wade Harlow<br>Sport Fishing</h1>
  <p class="hero-sub">Come Fish With Tampa Bay, FL Fishing Guide, Tampa Bay<br>Fishing Charter Most Respected Captain 25 Year Native Guide</p>
  <span class="btn">Book Now</span>
</section>

<section class="intro">
  <p class="eyebrow">Tampa Bay Fishing Charters Florida | Fishing Charters Tampa Bay</p>
  <h2 class="heading">Tampa Bay, Fishing Guide, Tampa Bay Fishing Charters</h2>
  <p class="intro-copy">Capt. Wade Harlow, With Over 20 Years' Experience, Native Fishing Charter Tampa Charter Captain Offering Full And Half Day Fishing Charters On The Waters Of Tampa Bay.<br>If You're Looking For a Great Fishing Charter Tampa Don't Hesitate To Contact Capt. Wade Or You Can Simply Book Your Trip Online Here.<br>Come Enjoy a Wonderful Day Fishing Charters Tampa For Tarpon, Snook, Redfish, Trout, Sharks, Cobia, Spanish Mackerel As Well As Others Aboard Capt. Wade Harlow Sport Fishing Charters Boat. Capt. Wade Will Work Hard To Ensure That You And Your Guests Have a Memorable Day Enjoying The Wonderful Gamefish That Tampa Bay Has To Offer.</p>
  <div class="badges"><div class="badge green"></div><div class="badge navy"></div></div>
</section>

<section class="locations">
  <p class="eyebrow">Four Convenient Locations on Every Corner of Tampa Bay</p>
  <h2 class="heading">Fishing Charters in Your Favorite Locations</h2>
  <div class="map" role="img" aria-label="Road map of the Tampa Bay area showing the pickup marina in St. Petersburg">
    <div class="map-card">Harbor Point Marina<br>4410 Gulfview Avenue South<br>St. Petersburg, FL 33711</div>
    <svg class="map-pin" width="34" height="46" viewBox="0 0 34 46"><path d="M17 2C8.7 2 2 8.7 2 17c0 11 15 27 15 27s15-16 15-27C32 8.7 25.3 2 17 2z" fill="#c9302c" stroke="#fff" stroke-width="2"/><circle cx="17" cy="17" r="6" fill="#fff"/></svg>
  </div>
  <span class="btn">Pickup Locations</span>
</section>

<section class="plans">
  <h2 class="heading">Choose a Plan That's Right for You</h2>
</section>
<article class="plan" style="left:162px">
  <div class="plan-photo" role="img" aria-label="Anglers releasing a leaping tarpon beside the boat" style="background:linear-gradient(160deg,#8a9a8e,#4e6f6e 60%,#2f4f57)"><span class="plan-tag">Half Day ( 4 Hour)</span></div>
  <div class="plan-price">Charter 1-3 People $399<br>4 People $499</div>
</article>
<article class="plan" style="left:460px">
  <div class="plan-photo" role="img" aria-label="Underwater view of tarpon swimming in green water" style="background:linear-gradient(160deg,#3fa6a5,#1e7f86 55%,#0f5864)"><span class="plan-tag">3/4 Day ( 6Hour )</span></div>
  <div class="plan-price">Charter 1-3 People $499<br>4 People $599</div>
</article>
<article class="plan" style="left:760px">
  <div class="plan-photo" role="img" aria-label="Angler holding up a large snook on the boat" style="background:linear-gradient(160deg,#6c9ad0,#4f80b6 50%,#8b8066)"><span class="plan-tag">Full Day ( 8Hours )</span></div>
  <div class="plan-price">Charter 1-3 People $599<br>4 People $699</div>
</article>

<section class="testimonials">
  <p class="eyebrow">What Say Your Client About Us</p>
  <h2 class="heading">Satisfied Customers</h2>
  <div class="quote" style="left:162px">
    <div class="quote-box"><b>&ldquo;</b> Capt. Wade has always been a 100%er for me <b>&rdquo;</b></div>
    <p class="quote-name">Dale Whitmore</p>
    <p class="quote-role">Outdoor Editor for Bayside Courier</p>
  </div>
  <div class="quote" style="left:461px">
    <div class="quote-box"><b>&ldquo;</b> Truly a master angler <b>&rdquo;</b></div>
    <p class="quote-name">Rita Calloway</p>
    <p class="quote-role">Former Hillsborough County Commissioner</p>
  </div>
  <div class="quote" style="left:760px">
    <div class="quote-box"><b>&ldquo;</b> Congratulations on winning the Harlan Brooks Celebrity Grand Slam Tournament <b>&rdquo;</b></div>
    <p class="quote-name">Martin Ellery</p>
    <p class="quote-role">Former Governor of Florida</p>
  </div>
  <div class="dots"><i class="on"></i><i></i><i></i><i></i></div>
</section>

<footer class="site-footer">
  <div class="contact">
    <div class="contact-row"><svg width="12" height="16" viewBox="0 0 12 16"><path d="M6 0a6 6 0 0 0-6 6c0 4.5 6 10 6 10s6-5.5 6-10a6 6 0 0 0-6-6zm0 8.5A2.5 2.5 0 1 1 6 3.5a2.5 2.5 0 0 1 0 5z" fill="#f5c33b"/></svg><span>210 Marsh Lane<br>Tampa, FL 33602</span></div>
    <div class="contact-row"><svg width="14" height="14" viewBox="0 0 24 24"><path d="M6.6 10.8a15 15 0 0 0 6.6 6.6l2.2-2.2c.3-.3.7-.4 1-.2 1.1.4 2.3.6 3.6.6.6 0 1 .4 1 1V20c0 .6-.4 1-1 1A17 17 0 0 1 3 4c0-.6.4-1 1-1h3.5c.6 0 1 .4 1 1 0 1.3.2 2.5.6 3.6.1.3 0 .7-.2 1z" fill="#f5c33b"/></svg><span>555-201-4438</span></div>
    <div class="contact-row"><svg width="15" height="11" viewBox="0 0 15 11"><rect width="15" height="11" rx="1" fill="#f5c33b"/><path d="M0 0l7.5 6L15 0" fill="none" stroke="#0b1a2c" stroke-width="1.2"/></svg><span>captwade@mailbox.example</span></div>
  </div>
  <div class="divider" style="left:378px"></div>
  <div class="info">
    <h4>Information</h4>
    <div class="info-links"><span>Home</span><span>Gallery</span><span>About Us</span><span>Contact</span><span>Pick Up Locations</span><span></span><span>Rates</span></div>
  </div>
  <div class="divider" style="left:760px"></div>
  <div class="footer-badges"><div class="badge green"></div><div class="badge navy"></div></div>
  <div class="socials">
    <i style="background:#3b5998"></i><i style="background:#cc2127"></i><i style="background:#dd4b39"></i><i style="background:#3b7cb8"></i><i style="background:#517fa4"></i><i style="background:#cb2027"></i>
  </div>
</footer>
<div class="copyright">Copyright &copy; 2016 reelcoveguide.example. All Rights Reserved.</div>

</body>
</html>
```